Unique Business Card Design

Unique Business Card design for our orthotic and prosthetic company. Our logo is on our website, color is light blue. Unique shape (artificial leg shaped, vertical, etc..) preferred. Logo, business name, individual name and basic demographics needed.

Industry/Entity Type

Business

Contact Information for Business Card

Logo, Industry, Phone # Logo, "Prosthetic & Orthotic Services" Place to add individual name and contact info

Colors
cee9f5

Requirements
Must have
• The icon must be there, placement of "Prosthetic & Orthotic Services" can be moved
Nice to have
• Like the mix of light blue, and a little darker blue. One design included the icons from my website which was a nice touch

```html
<!DOCTYPE html>
<html lang="en">
<head>
<meta charset="utf-8">
<title>Strideworks Inc. – Business Cards</title>
<link href="https://fonts.googleapis.com/css2?family=Open+Sans:wght@400;600;700&display=swap" rel="stylesheet">
<style>
  :root {
    --bg: #1d1d1f;
    --paper: #dcd9db;
    --royal: #31399b;
    --stripe: #6b6c70;
    --brand-blue: #1f78d1;
    --ink: #141414;
    --muted: #3a3a3c;
    --white: #ffffff;
  }
  * { margin: 0; padding: 0; box-sizing: border-box; }
  html, body {
    width: 1200px; height: 1000px; overflow: hidden;
    background: var(--bg);
    font-family: "Open Sans", Arial, sans-serif;
  }
  .card {
    position: absolute;
    width: 640px; height: 370px;
    border-radius: 28px;
    overflow: hidden;
    box-shadow: 0 18px 40px rgba(0,0,0,0.45);
  }
  .card--front { left: 110px; top: 100px; }
  .card--back { left: 450px; top: 520px; }
  .card__shapes { position: absolute; inset: 0; width: 100%; height: 100%; }

  .brand { position: absolute; display: flex; }
  .brand__dot { border-radius: 50%; flex: none; }
  .brand__text { display: flex; flex-direction: column; white-space: nowrap; }
  .brand__name { font-weight: 700; line-height: 1.2; letter-spacing: 0.3px; }
  .brand__tagline { border-top: 2px solid currentColor; padding-top: 2px; margin-top: 3px; }
  .brand__phone { font-weight: 700; line-height: 1.2; margin-top: 6px; }

  /* front brand: dot above stacked text */
  .card--front .brand {
    left: 40px; top: 62px;
    flex-direction: column; align-items: center; gap: 10px;
    color: var(--brand-blue);
  }
  .card--front .brand__dot { width: 72px; height: 72px; background: var(--brand-blue); }
  .card--front .brand__text { align-items: center; }
  .card--front .brand__name { font-size: 24px; }
  .card--front .brand__tagline { font-size: 13px; }
  .card--front .brand__phone { font-size: 32px; margin-top: 10px; }

  /* back brand: dot lower left, text upper right */
  .card--back .brand { left: 372px; top: 96px; gap: 10px; align-items: flex-end; color: var(--ink); }
  .card--back .brand__dot { width: 62px; height: 62px; background: var(--ink); margin-bottom: -34px; }
  .card--back .brand__name { font-size: 17px; }
  .card--back .brand__tagline { font-size: 10.5px; }
  .card--back .brand__phone { font-size: 24px; }

  .web-line {
    position: absolute; left: 392px; top: 128px;
    display: flex; align-items: center; gap: 8px;
    font-size: 14px; color: var(--muted);
  }
  .icon { width: 14px; height: 14px; flex: none; }

  .person { position: absolute; left: 44px; top: 150px; color: var(--white); }
  .person__name { font-weight: 700; font-size: 28px; line-height: 1.1; }
  .person__role { font-weight: 600; font-size: 22px; color: var(--brand-blue); margin-bottom: 22px; }
  .contact-list { list-style: none; }
  .contact-list li { display: flex; align-items: center; gap: 12px; font-size: 16px; line-height: 1.55; }
</style>
</head>
<body>

  <!-- Front -->
  <section class="card card--front">
    <svg class="card__shapes" viewBox="0 0 640 370" preserveAspectRatio="none" aria-hidden="true">
      <defs>
        <linearGradient id="darkPanelA" x1="0" y1="0" x2="1" y2="1">
          <stop offset="0" stop-color="#2b2c2e"/>
          <stop offset="1" stop-color="#4a4b4e"/>
        </linearGradient>
      </defs>
      <rect width="640" height="370" fill="var(--royal)"/>
      <path d="M300,90 Q470,48 640,42 V200 Q470,230 400,370 H300 Z" fill="var(--paper)"/>
      <path d="M400,370 Q470,230 640,200 V230 Q500,258 430,370 Z" fill="var(--stripe)"/>
      <path d="M0,0 H300 Q372,185 325,370 H0 Z" fill="url(#darkPanelA)"/>
    </svg>

    <div class="brand">
      <span class="brand__dot"></span>
      <div class="brand__text">
        <span class="brand__name">STRIDEWORKS INC.</span>
        <span class="brand__tagline">Prosthetic &amp; Orthotic Services</span>
        <span class="brand__phone">555.014.2290</span>
      </div>
    </div>

    <p class="web-line">
      <svg class="icon" viewBox="0 0 16 16"><circle cx="8" cy="8" r="7" fill="var(--brand-blue)"/><path d="M1,8 H15 M8,1 C4,5 4,11 8,15 M8,1 C12,5 12,11 8,15" stroke="#fff" stroke-width="1" fill="none"/></svg>
      www.youwebsitename.com
    </p>
  </section>

  <!-- Back -->
  <section class="card card--back">
    <svg class="card__shapes" viewBox="0 0 640 370" preserveAspectRatio="none" aria-hidden="true">
      <defs>
        <linearGradient id="darkPanelB" x1="0" y1="0" x2="1" y2="1">
          <stop offset="0" stop-color="#2b2c2e"/>
          <stop offset="1" stop-color="#4a4b4e"/>
        </linearGradient>
      </defs>
      <rect width="640" height="370" fill="var(--royal)"/>
      <path d="M300,90 Q470,48 640,42 V200 Q470,230 400,370 H300 Z" fill="var(--paper)"/>
      <path d="M400,370 Q470,230 640,200 V230 Q500,258 430,370 Z" fill="var(--stripe)"/>
      <path d="M0,0 H300 Q372,185 325,370 H0 Z" fill="url(#darkPanelB)"/>
    </svg>

    <div class="person">
      <h1 class="person__name">Daniel Reyes</h1>
      <p class="person__role">Director</p>
      <ul class="contact-list">
        <li>
          <svg class="icon" viewBox="0 0 16 16"><path d="M3,1 L6,1 L7,5 L5,6 C6,8 8,10 10,11 L11,9 L15,10 L15,13 C15,14 14,15 13,15 C6,15 1,10 1,3 C1,2 2,1 3,1 Z" fill="var(--brand-blue)"/></svg>
          +000 12345 6789
        </li>
        <li>
          <svg class="icon" viewBox="0 0 16 16"><rect x="1" y="3" width="14" height="10" rx="1" fill="var(--brand-blue)"/><path d="M1,4 L8,9 L15,4" stroke="#fff" stroke-width="1.2" fill="none"/></svg>
          yourname@email.com
        </li>
        <li>
          <svg class="icon" viewBox="0 0 16 16"><circle cx="8" cy="8" r="7" fill="var(--brand-blue)"/><path d="M1,8 H15 M8,1 C4,5 4,11 8,15 M8,1 C12,5 12,11 8,15" stroke="#fff" stroke-width="1" fill="none"/></svg>
          www.yoursitename.com
        </li>
      </ul>
    </div>

    <div class="brand">
      <span class="brand__dot"></span>
      <div class="brand__text">
        <span class="brand__name">STRIDEWORKS INC.</span>
        <span class="brand__tagline">Prosthetic &amp; Orthotic Services</span>
        <span class="brand__phone">555.014.2290</span>
      </div>
    </div>
  </section>

</body>
</html>
```